Business Card Design with new logo

Dorian Pelleway 4172
E 118th St Brenton, IL 62481
Cell: 217-555-0193
pellewayrestoration@mailvane.test

Classic Car Restoration Services Buy Sell Trade Consign

Dorian Pelleway 9698
Cell: 217-555-0193

```html
<!DOCTYPE html>
<html lang="en">
<head>
<meta charset="utf-8">
<title>Pelleway Restoration LLC — Business Card</title>
<link rel="stylesheet" href="https://fonts.googleapis.com/css2?family=Lato:wght@400;700&family=Raleway:wght@400&display=swap">
<style>
  :root {
    --backdrop: #262628;
    --red-light: #ee3b34;
    --red-dark: #bc2129;
    --paper: #ffffff;
    --navy: #14222e;
    --ink: #111111;
    --band-text: #e8ecef;
  }
  * { box-sizing: border-box; margin: 0; padding: 0; }
  html, body {
    width: 1200px; height: 1200px; overflow: hidden;
    background: var(--backdrop);
  }
  .sheet {
    width: 1200px; height: 1200px;
    display: flex; flex-direction: column; align-items: center; justify-content: center;
    gap: 44px;
  }
  .card {
    width: 840px; height: 480px; position: relative; overflow: hidden;
    box-shadow: 0 12px 30px rgba(0,0,0,.45);
  }

  /* Front */
  .card-front {
    background: linear-gradient(90deg, var(--red-light) 0 50%, var(--red-dark) 50% 100%);
    display: flex; align-items: center; justify-content: center;
  }
  .brand-front {
    display: flex; flex-direction: column; align-items: center; gap: 14px;
    color: var(--paper); font-family: "Lato", sans-serif; font-weight: 700;
    text-transform: uppercase;
  }
  .brand-front .brand-name { font-size: 74px; letter-spacing: 4px; line-height: 1; }
  .brand-front .brand-sub { font-size: 22px; letter-spacing: 16px; line-height: 1; }

  /* Back */
  .card-back { background: var(--paper); }
  .contact {
    position: absolute; left: 66px; top: 118px;
    font-family: "Lato", sans-serif; font-weight: 400; color: var(--ink);
    font-size: 24px; line-height: 1.25;
    list-style: none;
  }
  .contact li { display: flex; align-items: flex-start; gap: 16px; margin-bottom: 12px; }
  .contact .icon { width: 28px; height: 28px; flex: none; margin-top: 1px; }
  .brand-back {
    position: absolute; right: 40px; top: 40px; width: 250px; height: 320px;
    display: flex; align-items: center; justify-content: center;
  }
  .brand-back .brand-rotate {
    transform: rotate(90deg);
    display: flex; flex-direction: column; align-items: center; gap: 10px;
    font-family: "Lato", sans-serif; font-weight: 700; color: var(--navy);
    text-transform: uppercase; white-space: nowrap;
  }
  .brand-back .brand-name { font-size: 52px; letter-spacing: 3px; line-height: 1; }
  .brand-back .brand-sub { font-size: 16px; letter-spacing: 11px; line-height: 1; }
  .services {
    position: absolute; left: 0; right: 0; bottom: 0; height: 116px;
    background: var(--navy); color: var(--band-text);
    font-family: "Raleway", sans-serif; font-weight: 400; font-size: 24px;
    display: flex; align-items: center; padding-left: 72px; gap: 9px;
    white-space: nowrap;
  }
  .services .sep { opacity: .6; font-weight: 400; }
</style>
</head>
<body>
<main class="sheet">
  <section class="card card-front" aria-label="Card front">
    <div class="brand-front">
      <span class="brand-name">Pelleway</span>
      <span class="brand-sub">Restoration LLC</span>
    </div>
  </section>

  <section class="card card-back" aria-label="Card back">
    <ul class="contact">
      <li>
        <svg class="icon" viewBox="0 0 28 28" aria-hidden="true">
          <circle cx="14" cy="14" r="12" fill="none" stroke="#111" stroke-width="2"/>
          <path d="M10 8.5c1-.6 1.8-.3 2.3.6l.9 1.8c.3.7.1 1.3-.5 1.7l-.7.5c.5 1.6 1.5 2.8 3 3.7l.6-.6c.5-.5 1.2-.6 1.8-.2l1.6 1.1c.8.6.9 1.4.2 2.2-1 1.1-2.5 1.3-4 .5-3.3-1.8-5.3-4.7-5.9-8-.2-1.3.1-2.6.7-3.3z" fill="#111"/>
        </svg>
        <span>217-555-0193</span>
      </li>
      <li>
        <svg class="icon" viewBox="0 0 28 28" aria-hidden="true">
          <rect x="2" y="6" width="24" height="16" fill="#111"/>
          <path d="M3 7l11 9 11-9" fill="none" stroke="#fff" stroke-width="1.6"/>
        </svg>
        <span>pellewayrestoration@mailvane.test</span>
      </li>
      <li>
        <svg class="icon" viewBox="0 0 28 28" aria-hidden="true">
          <path d="M14 2c-5 0-8.5 3.6-8.5 8.3C5.5 16 14 26 14 26s8.5-10 8.5-15.7C22.5 5.6 19 2 14 2z" fill="#111"/>
          <circle cx="14" cy="10.5" r="3.3" fill="#fff"/>
        </svg>
        <span>Dorian Pelleway 4172<br>E 118th St Brenton, IL 62481</span>
      </li>
    </ul>

    <div class="brand-back">
      <div class="brand-rotate">
        <span class="brand-name">Pelleway</span>
        <span class="brand-sub">Restoration LLC</span>
      </div>
    </div>

    <div class="services">
      <span>Classic Car Restoration Services</span>
      <span class="sep">|</span><span>Buy</span>
      <span class="sep">|</span><span>Sell</span>
      <span class="sep">|</span><span>Trade</span>
      <span class="sep">|</span><span>Consign</span>
    </div>
  </section>
</main>
</body>
</html>
```